In Home Senior Care Agency Business Card Design Needed

At Silver Birch Helpers, we don't just work in the care-giving industry. We truly care.

We are dedicated to providing personable, hands-on and integrated caring services that aim to help people maintain safe and comfortable life standards within the familiar settings of their own homes.

We would like to see designs that use my logo colors obviously. The final design will be modern, yet professional and semi-minimalistic. It should communicate an well-established company that is innovative. We would also like the design to have that 'flat' design look. Ideally having the design roll over to the backend of the card. Most likely it will be printed on a Matte paper with a die cut (either 2 rounded corners -leaf cut) or all rounded.

Target Market(s)

Baby boomer generation. 45 years and older.

Industry/Entity Type

Business

Contact Information for Business Card

Text for Front:
Slogan somewhere "Our Family. Caring For Yours.”

Darren Whitlow
President

Cell: 917.284.6051
Phone: 917.512.7368
E: Darren@silverbirchhelpers.com
W: www.SilverBirchHelpers.com

Back:
-Meal Preparation
-Transportation
-Light Housekeeping
-Bathing Assistance
-Companionship

Font styles to use
Serif
Sans Serif

Requirements
Must have
• Flat, modern, professional design. Not too many colors. Match my colors in logo. Design of card must reflect from the front onto the back. Evenly spaced font.
Nice to have
• Try to work off current logo scheme, but logo may need to be redesigned.
Should not have
• Not too many colors.

```html
<!DOCTYPE html>
<html lang="en">
<head>
<meta charset="utf-8">
<title>Silver Birch Helpers — Business Card</title>
<link rel="stylesheet" href="https://fonts.googleapis.com/css2?family=Questrial&family=Didact+Gothic&display=swap">
<style>
  :root {
    --page: #ffffff;
    --green: #08683a;
    --paper: #ebecea;
    --white: #ffffff;
    --olive: #8d8a3b;
    --amber: #f5b13f;
    --ink: #3b3b3b;
    --shadow: rgba(0, 0, 0, 0.18);
  }
  * { box-sizing: border-box; margin: 0; padding: 0; }
  html, body {
    width: 1018px;
    height: 1200px;
    overflow: hidden;
    background: var(--page);
    font-family: "Questrial", "Didact Gothic", sans-serif;
  }
  .canvas { position: relative; width: 1018px; height: 1200px; }

  .card {
    position: absolute;
    left: 129px;
    width: 770px;
    height: 458px;
    border-radius: 110px 0 110px 0;
    overflow: hidden;
    box-shadow: 0 6px 14px var(--shadow);
  }
  .card--front { top: 122px; background: var(--green); color: var(--white); }
  .card--back { top: 642px; background: var(--paper); color: var(--ink); }

  .brand-name {
    position: absolute;
    left: 400px;
    width: 330px;
    text-align: center;
    font-family: "Questrial", sans-serif;
    font-size: 46px;
    line-height: 46px;
    letter-spacing: -0.5px;
  }
  .card--front .brand-name { top: 118px; color: var(--white); }
  .card--back .brand-name { top: 92px; color: var(--green); }

  .foliage {
    position: absolute;
    right: 0;
    bottom: 0;
    width: 320px;
    height: 250px;
    border-radius: 250px 0 0 0;
  }
  .card--front .foliage { background: radial-gradient(circle at 100% 100%, var(--olive) 55%, rgba(141, 138, 59, 0.55) 100%); }
  .card--back .foliage { background: radial-gradient(circle at 100% 100%, var(--amber) 55%, rgba(245, 177, 63, 0.55) 100%); }

  .contact-block { position: absolute; left: 64px; top: 150px; }
  .person-name { font-size: 23px; font-weight: 700; font-family: "Didact Gothic", sans-serif; letter-spacing: 0.2px; -webkit-text-stroke: 0.6px var(--white); }
  .person-title { font-size: 23px; margin-top: 8px; }
  .contact-list { list-style: none; margin-top: 20px; }
  .contact-list li {
    display: flex;
    align-items: center;
    gap: 10px;
    font-size: 22px;
    height: 34px;
  }
  .contact-list svg { width: 18px; height: 18px; flex: none; }

  .service-list { position: absolute; left: 64px; top: 208px; list-style: none; }
  .service-list li {
    display: flex;
    align-items: center;
    gap: 18px;
    font-size: 25px;
    height: 40px;
    letter-spacing: 0.3px;
  }
  .service-list li::before {
    content: "";
    width: 13px;
    height: 13px;
    border-radius: 50%;
    background: var(--amber);
  }
</style>
</head>
<body>
<main class="canvas">

  <section class="card card--front" aria-label="Card front">
    <div class="brand-name">Silver Birch<br>Helpers</div>

    <div class="contact-block">
      <p class="person-name">Darren Whitlow</p>
      <p class="person-title">President</p>
      <ul class="contact-list">
        <li>
          <svg viewBox="0 0 18 18" fill="none" stroke="currentColor" stroke-width="1.5"><rect x="3.5" y="1.5" width="11" height="15" rx="1.5"/><line x1="3.5" y1="13" x2="14.5" y2="13"/></svg>
          917.284.6051
        </li>
        <li>
          <svg viewBox="0 0 18 18" fill="currentColor"><path d="M5 1.5c1 0 1.6 2.6 1.6 3.4 0 .8-1.3 1.2-1.2 2 .3 1.8 1.8 4 3.3 5 .6.4 1.3-.9 2-.8.8.1 3 1.3 2.9 2.3-.1 1-1.8 2.5-3 2.2C6.5 14.8 2.7 9.7 2.8 5.1 2.8 3.3 4 1.5 5 1.5z"/></svg>
          917.512.7368
        </li>
        <li>
          <svg viewBox="0 0 18 18" fill="none" stroke="currentColor" stroke-width="1.5"><rect x="1.5" y="4" width="15" height="10"/><polyline points="1.5,4 9,10 16.5,4"/></svg>
          Darren@silverbirchhelpers.com
        </li>
        <li>
          <svg viewBox="0 0 18 18" fill="none" stroke="currentColor" stroke-width="1.3"><circle cx="9" cy="9" r="7.5"/><ellipse cx="9" cy="9" rx="3.2" ry="7.5"/><line x1="1.5" y1="9" x2="16.5" y2="9"/><line x1="9" y1="1.5" x2="9" y2="16.5"/></svg>
          www.SilverBirchHelpers.com
        </li>
      </ul>
    </div>

    <div class="foliage" role="img" aria-label="Olive leafy branch illustration in the lower right corner"></div>
  </section>

  <section class="card card--back" aria-label="Card back">
    <div class="brand-name">Silver Birch<br>Helpers</div>

    <ul class="service-list">
      <li>Meal Preparation</li>
      <li>Transportation</li>
      <li>Light Housekeeping</li>
      <li>Bathing Assistance</li>
      <li>Companionship</li>
    </ul>

    <div class="foliage" role="img" aria-label="Golden leafy branch illustration in the lower right corner"></div>
  </section>

</main>
</body>
</html>
```